Harlow Ridge Partners Business Cards

Design Business cards in a format where I can change the information and utilize a third party buisness card printing company

Contact Information for Business Card

Want Logo and Name on Back. Looking for Spot UV style shine on Logo. Probably Black background. Want smaller logo on front with contact details. Like rounded edges or something else interesting.

Requirements
Must have
• Strong masculine look.

```html
<!DOCTYPE html>
<html lang="en">
<head>
<meta charset="utf-8">
<title>Harlow Ridge Partners Business Cards</title>
<link rel="stylesheet" href="https://fonts.googleapis.com/css2?family=Cinzel:wght@400;600&family=Open+Sans:wght@400&display=swap">
<style>
  :root {
    --backdrop: #737373;
    --card: #121212;
    --ink-muted: #8c8c8c;
    --ink-soft: #a3a3a3;
    --silver: #c9c9c9;
    --white: #f4f4f4;
  }
  html, body {
    margin: 0;
    padding: 0;
    width: 1200px;
    height: 900px;
    overflow: hidden;
    background: var(--backdrop);
  }
  .canvas {
    position: relative;
    width: 1200px;
    height: 900px;
  }
  .card {
    position: absolute;
    top: 200px;
    width: 310px;
    height: 502px;
    background: var(--card);
    box-shadow: 2px 3px 6px rgba(0,0,0,0.35);
  }
  .card--front {
    left: 253px;
    border-radius: 62px 0 62px 0;
  }
  .card--back {
    left: 627px;
    border-radius: 0 62px 0 62px;
  }
  .brand-name {
    position: absolute;
    left: 0;
    right: 0;
    text-align: center;
    font-family: "Cinzel", serif;
    font-weight: 600;
    color: var(--ink-muted);
    letter-spacing: 1px;
    line-height: 1.15;
    margin: 0;
  }
  .card--front .brand-name {
    top: 330px;
    top: 130px;
    font-size: 28px;
  }
  .card--back .brand-name {
    top: 205px;
    font-size: 34px;
    color: var(--silver);
  }
  .contact {
    position: absolute;
    left: 34px;
    top: 298px;
    font-family: "Open Sans", sans-serif;
    color: var(--ink-muted);
  }
  .contact__name {
    font-family: "Cinzel", serif;
    font-weight: 400;
    font-size: 19px;
    letter-spacing: 0.5px;
    color: var(--ink-soft);
    margin: 0;
    line-height: 26px;
  }
  .contact__role {
    font-size: 14px;
    margin: 0 0 10px;
    line-height: 20px;
  }
  .contact__list {
    list-style: none;
    margin: 0;
    padding: 0;
  }
  .contact__item {
    display: flex;
    align-items: center;
    font-size: 14.5px;
    line-height: 18px;
  }
  .contact__icon {
    width: 11px;
    height: 11px;
    margin-right: 7px;
    fill: var(--ink-muted);
  }
  .contact__address {
    font-size: 14.5px;
    line-height: 18px;
    margin: 9px 0 0;
    font-style: normal;
  }
  .website {
    position: absolute;
    left: 0;
    right: 0;
    top: 443px;
    text-align: center;
    font-family: "Open Sans", sans-serif;
    font-size: 14px;
    letter-spacing: 0.6px;
    color: var(--white);
    margin: 0;
  }
</style>
</head>
<body>
<main class="canvas">

  <section class="card card--front" aria-label="Card front">
    <p class="brand-name">Harlow Ridge<br>Partners</p>

    <div class="contact">
      <h1 class="contact__name">DANIEL WHITMORE</h1>
      <p class="contact__role">Managing Director</p>
      <ul class="contact__list">
        <li class="contact__item">
          <svg class="contact__icon" viewBox="0 0 12 12" aria-hidden="true"><path d="M1 4c0-1.5 2-3 5-3s5 1.5 5 3v1H8.5V3.8h-5V5H1zM2.5 6h7l1 5h-9z"/></svg>
          044-123 456 789
        </li>
        <li class="contact__item">
          <svg class="contact__icon" viewBox="0 0 12 12" aria-hidden="true"><path d="M3.5 0h5a1 1 0 0 1 1 1v10a1 1 0 0 1-1 1h-5a1 1 0 0 1-1-1V1a1 1 0 0 1 1-1zm0 1.5v7.5h5V1.5zM6 9.8a.7.7 0 1 0 0 1.4.7.7 0 0 0 0-1.4z"/></svg>
          044-123 456 789
        </li>
        <li class="contact__item">
          <svg class="contact__icon" viewBox="0 0 12 12" aria-hidden="true"><path d="M0 2.5h12v7H0zM1 3.3l5 3.5 5-3.5v-.1H1z"/></svg>
          info@webname.com
        </li>
        <li class="contact__item">
          <svg class="contact__icon" viewBox="0 0 12 12" aria-hidden="true"><circle cx="6" cy="6" r="5.5"/></svg>
          www.websitename.com
        </li>
      </ul>
      <address class="contact__address">12345, Address Goes Here<br>Country Name, 123456.</address>
    </div>
  </section>

  <section class="card card--back" aria-label="Card back">
    <p class="brand-name">Harlow Ridge<br>Partners</p>
    <p class="website">www.harlowridgepartners.com</p>
  </section>

</main>
</body>
</html>
```